Business Card for Flight Instructor/Commercial Pilot

I need a business card for myself as a Flight Instructor. I'm a certificated flight instructor at a local flight school in St Paul, MN and want to have a business card that I can give out both to prospective students and also to prospective employers in commercial/business aviation. The business card should have a few elements to it (my name, my position, and my ZRT certifications:
Dorian Welkes, MBA
Flight Instructor
CFI, CFII, AGI, IGI
Then lastly, I'd like it to include my phone number for calls or texts, my email address, and my Corvanet url. I'll provide all of these at a later point.

If we can include some kind of aviation graphic, that's great, but I don't currently have a logo and I don't necessarily need one, so don't feel like a logo is required here, it's not. I'm but I'm open to whatever you might put together. But I honestly don't need a logo, just good design with a simple graphic element to draw a little interest.
I'd also like to add a short tag line. A few ideas I have are:
- Fly Smart. Stay Humble. Never Stop Learning.
- Train smart. Fly safe. Have fun.
- Master the craft. Enjoy the flight.

For the back side, I'm open to ideas on what to put there. maybe the tagline could go there, or a QR code for my Corvanet page, or maybe something else.

Target audience is both prospective students who are interested in learning to fly (or adding more ratings) and commercial aviation companies that could be potential employer for me in commercial aviation. Trying to portray a sense of professionalism, trust, and high level of competency.

The business card doesn’t have to be standard (rectangular with square corners) and I’m open to suggestions for based on the design.
Lastly, I just don't want the design created by AI.
Let me know if you need any further info. Thanks!

```html
<!DOCTYPE html>
<html lang="en">
<head>
<meta charset="utf-8">
<title>Dorian Welkes – Flight Instructor Business Card</title>
<link rel="stylesheet" href="https://fonts.googleapis.com/css2?family=Poppins:wght@400;500;600;700&display=swap">
<style>
  :root {
    --stage: #2c3036;
    --card: #ffffff;
    --teal: #3c7893;
    --graphite: #4a4a4c;
    --ink: #3d3d40;
    --muted: #5f6166;
    --rule: #6f737a;
  }
  html, body {
    margin: 0;
    width: 1200px;
    height: 985px;
    overflow: hidden;
    background: var(--stage);
    font-family: "Poppins", sans-serif;
  }
  .stage {
    position: relative;
    width: 1200px;
    height: 985px;
  }
  .card {
    position: absolute;
    left: 280px;
    width: 640px;
    height: 366px;
    border-radius: 28px;
    background: var(--card);
    overflow: hidden;
    box-shadow: 0 14px 32px rgba(0,0,0,.35);
  }
  .card--front { top: 80px; }
  .card--back { top: 536px; }

  .front-art {
    position: absolute;
    inset: 0;
  }

  .wordmark {
    position: absolute;
    display: flex;
    align-items: center;
    gap: 10px;
    color: var(--teal);
    font-weight: 700;
    white-space: nowrap;
  }
  .wordmark__dot {
    border-radius: 50%;
    background: var(--graphite);
  }
  .card--front .wordmark {
    left: 40px;
    top: 62px;
    font-size: 28px;
    letter-spacing: .3px;
  }
  .card--front .wordmark__dot { width: 22px; height: 22px; }

  .divider {
    position: absolute;
    left: 40px;
    top: 122px;
    width: 250px;
    height: 1px;
    background: var(--rule);
  }
  .identity {
    position: absolute;
    left: 40px;
    top: 134px;
  }
  .identity__name {
    margin: 0;
    color: var(--teal);
    font-weight: 600;
    font-size: 19px;
    line-height: 1.3;
  }
  .identity__role, .identity__certs {
    margin: 0;
    color: var(--muted);
    font-size: 12.5px;
    line-height: 1.5;
  }
  .tick {
    position: absolute;
    left: 206px;
    top: 246px;
    width: 1px;
    height: 30px;
    background: var(--teal);
    transform: rotate(18deg);
  }
  .contacts {
    position: absolute;
    left: 196px;
    top: 288px;
    margin: 0;
    padding: 0;
    list-style: none;
    color: var(--ink);
    font-size: 15px;
    line-height: 1.5;
  }
  .contacts li {
    display: flex;
    align-items: center;
    gap: 8px;
  }
  .contacts__icon {
    width: 16px;
    height: 16px;
    flex: none;
  }
  .calls {
    position: absolute;
    right: 32px;
    top: 160px;
    text-align: right;
    color: #ffffff;
  }
  .calls__label {
    margin: 0;
    font-weight: 600;
    font-size: 14px;
    letter-spacing: .3px;
  }
  .calls__number {
    margin: 0;
    font-size: 16px;
  }

  .card--back .wordmark {
    left: 0;
    right: 0;
    top: 130px;
    justify-content: center;
    font-size: 46px;
  }
  .card--back .wordmark__dot { width: 34px; height: 34px; }
  .back-certs {
    position: absolute;
    left: 0;
    right: 0;
    top: 206px;
    margin: 0;
    text-align: center;
    color: var(--graphite);
    font-size: 17px;
    letter-spacing: .5px;
  }
</style>
</head>
<body>
<main class="stage">

  <section class="card card--front" aria-label="Business card front">
    <svg class="front-art" width="640" height="366" viewBox="0 0 640 366" aria-hidden="true">
      <path d="M60 0 Q470 40 520 366 L640 366 L640 0 Z" fill="#3c7893"/>
      <path d="M60 0 Q470 40 520 366" fill="none" stroke="#ffffff" stroke-width="16"/>
      <path d="M25 0 Q435 44 487 366" fill="none" stroke="#4a4a4c" stroke-width="8"/>
      <path d="M0 6 Q410 48 460 366" fill="none" stroke="#4a4a4c" stroke-width="1.2"/>
    </svg>

    <div class="wordmark"><span class="wordmark__dot"></span>Dorian Welkes</div>
    <div class="divider"></div>

    <div class="identity">
      <p class="identity__name">Dorian Welkes, MBA</p>
      <p class="identity__role">Flight Instructor</p>
      <p class="identity__certs">CFI, CFII, AGI, IGI</p>
    </div>

    <div class="tick"></div>

    <ul class="contacts">
      <li>
        <svg class="contacts__icon" viewBox="0 0 16 16" aria-hidden="true">
          <circle cx="8" cy="8" r="8" fill="#3c7893"/>
          <rect x="4" y="5" width="8" height="6" rx="1" fill="#ffffff"/>
          <path d="M4.3 5.4 L8 8.4 L11.7 5.4" fill="none" stroke="#3c7893" stroke-width="1"/>
        </svg>
        company@mailbay.com
      </li>
      <li>
        <svg class="contacts__icon" viewBox="0 0 16 16" aria-hidden="true">
          <circle cx="8" cy="8" r="8" fill="#3c7893"/>
        </svg>
        Corvanet url.com
      </li>
    </ul>

    <div class="calls">
      <p class="calls__label">CALLS or TEXTS</p>
      <p class="calls__number">(555) 014-2290</p>
    </div>
  </section>

  <section class="card card--back" aria-label="Business card back">
    <div class="wordmark"><span class="wordmark__dot"></span>Dorian Welkes</div>
    <p class="back-certs">CFI, CFII, AGI, IGI</p>
  </section>

</main>
</body>
</html>
```